Copper lark buildworks

Copper lark buildworks is a small construction company.
Who is a licenced builder, Carpenter, joiner,
working on heritage ,new build, speacial projects and sometimes furniture

Industry/Entity Type

Construction

```html
<!DOCTYPE html>
<html lang="en">
<head>
<meta charset="utf-8">
<title>Copper lark buildworks – business card</title>
<link href="https://fonts.googleapis.com/css2?family=Open+Sans:wght@400;600;700&display=swap" rel="stylesheet">
<style>
  :root {
    --navy: #123f72;
    --green: #6ab42d;
    --paper: #fcfcfb;
    --backdrop: #e6e8eb;
    --ink-light: #ffffff;
  }
  * { box-sizing: border-box; margin: 0; padding: 0; }
  html, body {
    width: 1200px;
    height: 800px;
    overflow: hidden;
    background: var(--backdrop);
    font-family: "Open Sans", Arial, sans-serif;
  }
  .card {
    position: absolute;
    left: 50px;
    top: 85px;
    width: 1100px;
    height: 630px;
    background: var(--paper);
    overflow: hidden;
    box-shadow: 0 6px 24px rgba(0,0,0,0.12);
  }
  .card-graphics {
    position: absolute;
    inset: 0;
  }
  .brand-name {
    position: absolute;
    left: 90px;
    top: 205px;
    width: 440px;
    font-weight: 700;
    font-size: 64px;
    line-height: 1.02;
    color: var(--green);
  }
  .trade-summary {
    position: absolute;
    left: 90px;
    top: 490px;
    font-size: 25px;
    line-height: 1.3;
    color: var(--navy);
  }
  .contact-panel {
    position: absolute;
    left: 700px;
    top: 0;
    width: 390px;
    height: 100%;
    color: var(--ink-light);
  }
  .person-name {
    position: absolute;
    top: 95px;
    left: 0;
    font-weight: 600;
    font-size: 50px;
    letter-spacing: 1px;
    line-height: 1;
    white-space: nowrap;
  }
  .person-role {
    position: absolute;
    top: 160px;
    left: 4px;
    font-size: 30px;
    letter-spacing: 7px;
    line-height: 1;
    white-space: nowrap;
  }
  .contact-line {
    position: absolute;
    font-size: 28px;
    line-height: 1.2;
    white-space: nowrap;
  }
  .contact-address { top: 282px; }
  .contact-email { top: 390px; left: 10px; }
  .contact-phone { top: 478px; left: 30px; }
  .licence-note {
    position: absolute;
    top: 562px;
    left: 60px;
    font-size: 25px;
    white-space: nowrap;
  }
</style>
</head>
<body>
  <div class="card">
    <svg class="card-graphics" width="1100" height="630" viewBox="0 0 1100 630" aria-hidden="true">
      <rect x="660" y="0" width="440" height="630" fill="var(--navy)"/>
      <rect x="632" y="0" width="5" height="260" fill="var(--green)"/>
      <rect x="632" y="545" width="5" height="85" fill="var(--green)"/>
      <path fill="var(--paper)" d="M610 282 H664 L680 298 V328 L664 344 H610 Z"/>
      <path fill="var(--paper)" d="M610 372 H664 L680 388 V418 L664 434 H610 Z"/>
      <path fill="var(--paper)" d="M610 462 H664 L680 478 V508 L664 524 H610 Z"/>
      <path fill="var(--green)" d="M639 298 L622 313 H627 V328 H635 V320 H643 V328 H651 V313 H656 Z"/>
      <rect x="623" y="393" width="32" height="21" fill="var(--green)"/>
      <path d="M623 393 L639 406 L655 393" fill="none" stroke="var(--paper)" stroke-width="2"/>
      <path fill="var(--green)" d="M631 480 h7 l3 8 -4 3 q3 7 9 10 l3 -4 8 3 v7 q-2 3 -6 3 q-20 -4 -24 -24 q0 -4 4 -6 z"/>
    </svg>

    <div class="brand-name">Copper lark buildworks</div>

    <p class="trade-summary">Carpenter, joiner, working on<br>heritage new\build speacial<br>projects and sometimes furniture</p>

    <div class="contact-panel">
      <h1 class="person-name">ROWAN HALE</h1>
      <p class="person-role">DIRECTOR</p>
      <p class="contact-line contact-address">412 kowhai lane west<br>wellington 604</p>
      <p class="contact-line contact-email">copperlark@mail.com</p>
      <p class="contact-line contact-phone">09 555 0142</p>
      <p class="licence-note">licenced builder</p>
    </div>
  </div>
</body>
</html>
```